New Business Card Design Project

Use the flyer uploaded and website www.brightoakbuilders.example for inspiration.
List Our Services on Backside of business cards
Marcus Dell
Harborline Renovations Inc.
Licensed General Contractors
555-014-7390

Contact Information for Business Card

Use the flyer uploaded and website www.brightoakbuilders.example for inspiration. List Our Services on Backside of business cards Marcus Dell Harborline Renovations Inc. Licensed General Contractors 555-014-7390

```html
<!DOCTYPE html>
<html lang="en">
<head>
<meta charset="utf-8">
<title>Harborline Renovations – Business Cards</title>
<link href="https://fonts.googleapis.com/css2?family=Montserrat:wght@400;500;700&family=Open+Sans:wght@400;700&display=swap" rel="stylesheet">
<style>
  :root {
    --backdrop: #2b2622;
    --card: #161616;
    --ink: #ffffff;
    --ink-soft: #d9d9d9;
    --rule: #e6e6e6;
  }
  * { margin: 0; padding: 0; box-sizing: border-box; }
  html, body { width: 1200px; height: 716px; overflow: hidden; }
  body {
    background: var(--backdrop);
    display: flex;
    align-items: center;
    justify-content: center;
    gap: 40px;
    font-family: "Open Sans", sans-serif;
    color: var(--ink);
  }
  .card {
    position: relative;
    width: 540px;
    height: 309px;
    background: var(--card);
    border-radius: 4px;
    box-shadow: 0 10px 24px rgba(0,0,0,.45);
    overflow: hidden;
  }
  .brand-name {
    font-family: "Montserrat", sans-serif;
    font-weight: 500;
    text-transform: uppercase;
    letter-spacing: 2px;
    color: var(--ink);
  }

  /* Services side */
  .card--services .brand-name {
    position: absolute;
    top: 58px; left: 0; right: 0;
    text-align: center;
    font-size: 20px;
  }
  .services-heading {
    position: absolute;
    top: 112px; left: 36px; right: 36px;
    display: flex;
    align-items: center;
    gap: 14px;
    font-family: "Open Sans", sans-serif;
    font-weight: 700;
    font-size: 15px;
    letter-spacing: .5px;
  }
  .services-heading::before,
  .services-heading::after {
    content: "";
    flex: 1;
    height: 1.5px;
    background: var(--rule);
  }
  .services-list {
    position: absolute;
    top: 148px; left: 36px; right: 30px;
    display: grid;
    grid-template-columns: 1fr 1fr;
    column-gap: 18px;
    list-style: none;
  }
  .services-list li {
    display: flex;
    align-items: center;
    gap: 6px;
    font-size: 12.5px;
    line-height: 21px;
    color: var(--ink-soft);
    white-space: nowrap;
  }
  .tick { width: 11px; height: 11px; flex: none; }

  /* Contact side */
  .contact-block {
    position: absolute;
    left: 34px; top: 150px;
    width: 220px;
  }
  .person-name {
    font-family: "Montserrat", sans-serif;
    font-weight: 700;
    font-size: 23px;
  }
  .person-title {
    font-family: "Montserrat", sans-serif;
    font-size: 13px;
    color: var(--ink-soft);
    padding: 4px 0 9px;
    border-bottom: 1.5px solid var(--rule);
  }
  .contact-line {
    display: flex;
    align-items: center;
    gap: 8px;
    font-family: "Montserrat", sans-serif;
    font-size: 13px;
    margin-top: 12px;
    color: var(--ink-soft);
  }
  .contact-line svg { width: 13px; height: 13px; flex: none; }
  .card--contact .brand-name {
    position: absolute;
    top: 112px; right: 34px;
    font-size: 17px;
    text-align: right;
    width: 220px;
    line-height: 1.35;
  }
  .web-block {
    position: absolute;
    right: 34px; bottom: 36px;
    width: 240px;
    border-top: 1.5px solid var(--rule);
    padding-top: 10px;
  }
  .web-block .contact-line { margin-top: 0; font-size: 12.5px; }
</style>
</head>
<body>

  <section class="card card--services" aria-label="Card back: services">
    <div class="brand-name">Harborline Renovations</div>
    <h2 class="services-heading">OUR SERVICES</h2>
    <ul class="services-list">
      <li><svg class="tick" viewBox="0 0 12 12"><rect x=".75" y=".75" width="10.5" height="10.5" fill="none" stroke="#fff" stroke-width="1.5"/><path d="M3 6.2l2 2 4-4.6" fill="none" stroke="#fff" stroke-width="1.6"/></svg>Remodel: Kitchen &amp; Bath</li>
      <li><svg class="tick" viewBox="0 0 12 12"><rect x=".75" y=".75" width="10.5" height="10.5" fill="none" stroke="#fff" stroke-width="1.5"/><path d="M3 6.2l2 2 4-4.6" fill="none" stroke="#fff" stroke-width="1.6"/></svg>Plumbing: Repairs &amp; Upgrades</li>
      <li><svg class="tick" viewBox="0 0 12 12"><rect x=".75" y=".75" width="10.5" height="10.5" fill="none" stroke="#fff" stroke-width="1.5"/><path d="M3 6.2l2 2 4-4.6" fill="none" stroke="#fff" stroke-width="1.6"/></svg>Painting: Interior &amp; Exterior</li>
      <li><svg class="tick" viewBox="0 0 12 12"><rect x=".75" y=".75" width="10.5" height="10.5" fill="none" stroke="#fff" stroke-width="1.5"/><path d="M3 6.2l2 2 4-4.6" fill="none" stroke="#fff" stroke-width="1.6"/></svg>Energy-Efficient Upgrades</li>
      <li><svg class="tick" viewBox="0 0 12 12"><rect x=".75" y=".75" width="10.5" height="10.5" fill="none" stroke="#fff" stroke-width="1.5"/><path d="M3 6.2l2 2 4-4.6" fill="none" stroke="#fff" stroke-width="1.6"/></svg>Flooring: Carpet, Vinyl, Wood</li>
      <li><svg class="tick" viewBox="0 0 12 12"><rect x=".75" y=".75" width="10.5" height="10.5" fill="none" stroke="#fff" stroke-width="1.5"/><path d="M3 6.2l2 2 4-4.6" fill="none" stroke="#fff" stroke-width="1.6"/></svg>Deck &amp; Patio Construction</li>
      <li><svg class="tick" viewBox="0 0 12 12"><rect x=".75" y=".75" width="10.5" height="10.5" fill="none" stroke="#fff" stroke-width="1.5"/><path d="M3 6.2l2 2 4-4.6" fill="none" stroke="#fff" stroke-width="1.6"/></svg>Window &amp; Door Replacement</li>
    </ul>
  </section>

  <section class="card card--contact" aria-label="Card front: contact">
    <div class="contact-block">
      <h1 class="person-name">Marcus Dell</h1>
      <p class="person-title">Licensed General Contractors</p>
      <p class="contact-line">
        <svg viewBox="0 0 14 14"><path d="M3 1.2l2.2 2.6-1.2 1.6c.8 1.8 2.2 3.2 4 4l1.6-1.2 2.6 2.2-1.2 2C6.4 12.2 1.8 7.6 1 2.4z" fill="none" stroke="#fff" stroke-width="1.2" stroke-linejoin="round"/></svg>
        555-014-7390
      </p>
    </div>

    <div class="brand-name">Harborline Renovations</div>

    <div class="web-block">
      <p class="contact-line">
        <svg viewBox="0 0 14 14"><circle cx="7" cy="7" r="5.8" fill="none" stroke="#fff" stroke-width="1.2"/><ellipse cx="7" cy="7" rx="2.6" ry="5.8" fill="none" stroke="#fff" stroke-width="1.1"/><path d="M1.2 7h11.6M2.2 4h9.6M2.2 10h9.6" stroke="#fff" stroke-width="1"/></svg>
        www.brightoakbuilders.example
      </p>
    </div>
  </section>

</body>
</html>
```